TESOL in Vietnam

My company needs banner ad designs (5 different sizes) to be placed on various websites to promote our product.

Our product is a 4-week Teaching English to Speakers of other Languages (TESOL) training program in Ho Chi Minh City, Vietnam. TESOL certification is the minimum qualification to work as an English language teacher in many parts of the world.

Basically, we want people to enroll in our 4 week Teacher training course in HCMC, Vietnam, with the view of teaching English in Vietnam.

You can see who we are and what we do here: www.brightlarklessons-asia.com

Key pointers include:

1. Our company logo (which includes our name & slogan) will be prominent in the banner - see attached

2. Our website address will be prominent:
www.brightlarklessons-asia.com

3. The main selling points for our product will be listed in the banner - note below:

Our TESOL training program in Ho Chi Minh City, Vietnam includes:

- the 4-week TESOL course (Australian Government accredited, internationally recognised);
- western standard accommodation within a 4 minute walk of my school for the duration of the course (4-weeks); and
- a guaranteed English teaching position at the end, paid at market rates.

4. the color scheme should be bright and eye catching - a lot of red, orange and alike.

I hope this information is helpful.

Martin Halloway

Hi All Note the rough sketch that I have added to the brief associated with this project. Cheers Martin

Target Market(s)

Men & women - 22 to 35 years of aage
Adventurous
Love to travel

Industry/Entity Type

Accommodation

Font styles to use
Other font styles liked:
• Calibri

Colors
eb1f27

Requirements
Must have
• Sense of fun
Credibility
Nice to have
• bright colors
Should not have
• Dour

```html
<!DOCTYPE html>
<html lang="en">
<head>
<meta charset="utf-8">
<title>TESOL in Vietnam – Banner Set</title>
<link rel="stylesheet" href="https://fonts.googleapis.com/css2?family=Cabin+Condensed:wght@400;600;700&family=PT+Sans:wght@400;700&display=swap">
<style>
  :root{
    --board:#2b2b2b;
    --red:#eb1f27;
    --red-mid:#c4161c;
    --maroon:#7b0a0f;
    --maroon-deep:#6a070b;
    --yellow:#ffe21f;
    --gold:#f2c230;
    --white:#ffffff;
    --ink:#1a1a1a;
    --grey:#555555;
  }
  *{box-sizing:border-box;margin:0;padding:0}
  html,body{width:1200px;height:826px;overflow:hidden}
  body{background:var(--board);position:relative;font-family:"PT Sans",Arial,sans-serif;color:var(--white)}
  .size-list{position:absolute;left:28px;top:26px;font:700 19px/28px "PT Sans",Arial,sans-serif;color:var(--white)}
  .size-label{position:absolute;font:700 19px/1 "PT Sans",Arial,sans-serif;color:var(--white)}
  .banner{position:absolute;overflow:hidden}
  .brand{display:flex;align-items:center;gap:6px;color:var(--red);font-family:"Cabin Condensed",Arial,sans-serif;font-weight:700;line-height:1.05}
  .brand-dot{flex:none;border-radius:50%;background:var(--red)}

  /* Skyscraper 120x600 */
  .sky{left:232px;top:154px;width:113px;height:566px;background:var(--maroon);border:4px solid var(--red-mid)}
  .sky-top{position:absolute;left:0;top:0;width:105px;height:160px}
  .sky .brand{position:absolute;left:8px;top:62px;width:90px;flex-direction:column;text-align:center;font-size:15px;gap:8px}
  .sky-company{position:absolute;top:170px;width:100%;text-align:center;font:700 12px/1.15 "Cabin Condensed",Arial,sans-serif}
  .sky-company b{display:block;font-size:19px}
  .sky-headline{position:absolute;top:220px;width:100%;text-align:center;color:var(--yellow);font:700 25px/32px "Cabin Condensed",Arial,sans-serif;letter-spacing:2px}
  .sky-points{position:absolute;top:323px;left:0;width:100%;text-align:center;font-size:10.5px;line-height:1.2}
  .sky-points li{list-style:none;height:57px;padding-top:7px;border-top:1px solid var(--gold)}
  .sky-points strong{display:block;font-size:13.5px}
  .sky-url{position:absolute;top:494px;left:0;width:100%;text-align:center;color:var(--yellow);font:600 15px/1.05 "Cabin Condensed",Arial,sans-serif;border-top:1px solid var(--gold);padding-top:6px}

  /* 468x60 */
  .leader-s{left:378px;top:157px;width:441px;height:57px;background:var(--white)}
  .leader-s .brand{position:absolute;left:14px;top:14px;font-size:17px}
  .leader-s-red{position:absolute;left:190px;top:0;width:251px;height:57px;background:var(--red-mid);clip-path:polygon(8px 0,100% 0,100% 100%,0 100%)}
  .leader-s-head{position:absolute;left:14px;top:5px;color:var(--yellow);font:700 12px/16px "Cabin Condensed",Arial,sans-serif}
  .leader-s-cols{position:absolute;left:62px;top:4px;display:flex;font-size:8px;line-height:9px;text-align:center}
  .leader-s-cols span{padding:0 5px;border-left:1px solid var(--white)}
  .leader-s-cols span:first-child{border-left:0}
  .leader-s-url{position:absolute;left:30px;top:39px;width:170px;height:15px;border-radius:8px;background:var(--yellow);color:var(--ink);font:700 9.5px/15px "PT Sans",Arial,sans-serif;text-align:center}

  /* 728x90 */
  .leader{left:372px;top:289px;width:688px;height:85px;background:var(--white)}
  .leader .brand{position:absolute;left:22px;top:28px;font-size:22px;gap:10px}
  .leader-globe{position:absolute;left:288px;top:16px;width:58px;height:58px;border-radius:50%;background:radial-gradient(circle at 35% 35%,#f39a9a,#a31b1f 70%)}
  .leader-panel{position:absolute;left:336px;top:0;width:352px;height:85px}
  .leader-head{position:absolute;left:42px;top:0;width:310px;height:20px;background:var(--maroon);color:var(--yellow);font:700 16px/20px "Cabin Condensed",Arial,sans-serif;letter-spacing:4px;text-align:center}
  .leader-points{position:absolute;left:30px;top:22px;font-size:10.5px;line-height:14.5px}
  .leader-points li{list-style:none;display:flex;align-items:center;gap:4px}
  .leader-points li:nth-child(2){padding-left:55px}
  .leader-points li:nth-child(3){padding-left:120px}
  .leader-points li::before{content:"";width:9px;height:9px;border-radius:50%;background:var(--yellow)}
  .leader-points strong{font-size:13px}
  .leader-url{position:absolute;left:42px;top:66px;width:310px;height:19px;background:var(--maroon);color:var(--yellow);font:700 14px/19px "PT Sans",Arial,sans-serif;text-align:center}

  /* 234x60 */
  .half{left:371px;top:421px;width:220px;height:56px;background:var(--white);border:3px solid var(--red-mid)}
  .half .brand{position:absolute;left:12px;top:9px;font-size:15px}
  .half-url{position:absolute;right:6px;bottom:3px;color:var(--ink);font-size:9px}

  /* 300x250 */
  .rect{left:634px;top:420px;width:283px;height:236px;background:var(--maroon);border:4px solid var(--red-mid)}
  .rect-top{position:absolute;left:0;top:0;width:275px;height:160px}
  .rect .brand{position:absolute;left:16px;top:30px;font-size:22px;gap:10px}
  .rect-copy{position:absolute;right:9px;top:96px;text-align:right;font-size:11.5px;line-height:1.05}
  .rect-copy strong{font-size:17px}
  .rect-copy p{margin-bottom:5px}
  .rect-copy .big{font-size:20px;font-weight:700}
  .rect-copy .mid{font-size:20px}
  .rect-guarantee{position:absolute;left:7px;top:176px;font-size:13px;font-weight:700;white-space:nowrap}
  .rect-guarantee strong{font-size:16px}
  .rect-url{position:absolute;left:7px;top:201px;width:261px;height:28px;border-radius:5px;background:var(--yellow);color:var(--ink);font:700 13.5px/28px "PT Sans",Arial,sans-serif;text-align:center}
</style>
</head>
<body>
  <div class="size-list">468 X 60<br>728 X 90<br>234 X 60<br>120 X 600<br>300 X 250</div>

  <section class="banner sky" aria-label="120 by 600 banner">
    <svg class="sky-top" viewBox="0 0 105 160" aria-hidden="true"><path d="M0 0H105V136Q60 150 0 160Z" fill="#ffffff"/></svg>
    <div class="brand"><span class="brand-dot" style="width:22px;height:22px"></span>Bright Lark Lessons Asia</div>
    <div class="sky-company">BRIGHT LARK<b>LESSONS</b>ASIA COMPANY</div>
    <div class="sky-headline">TESOL<br>IN<br>VIETNAM</div>
    <ul class="sky-points">
      <li><strong>Australian</strong>Government<br>accredited</li>
      <li><strong>FREE</strong>accommodation<br>in Ho Chi Minh City</li>
      <li><strong>Guaranteed</strong>teaching job<br>at the end</li>
    </ul>
    <div class="sky-url">www.<br>brightlarklessons-<br>asia.com</div>
  </section>

  <div class="size-label" style="left:391px;top:124px">468 X 60</div>
  <section class="banner leader-s" aria-label="468 by 60 banner">
    <div class="brand"><span class="brand-dot" style="width:18px;height:18px"></span>Bright Lark Lessons Asia</div>
    <div class="leader-s-red">
      <div class="leader-s-head">TESOL IN<br>VIETNAM</div>
      <div class="leader-s-cols">
        <span>Australian<br>Government<br>accredited</span>
        <span>F R E E<br>accommodation in<br>Ho Chi Minh City</span>
        <span>Guaranteed<br>teaching job<br>at the end</span>
      </div>
      <div class="leader-s-url">www.brightlarklessons-asia.com</div>
    </div>
  </section>

  <div class="size-label" style="left:391px;top:250px">728 X 60</div>
  <section class="banner leader" aria-label="728 by 90 banner">
    <div class="brand"><span class="brand-dot" style="width:26px;height:26px"></span>Bright Lark Lessons Asia</div>
    <svg class="leader-panel" viewBox="0 0 352 85" aria-hidden="true">
      <path d="M30 0H352V85H12Q34 42 30 0Z" fill="#ffe21f"/>
      <path d="M38 0H352V85H20Q42 42 38 0Z" fill="#c4161c"/>
    </svg>
    <div class="leader-globe" role="img" aria-label="Globe illustration"></div>
    <div class="leader-panel">
      <div class="leader-head">TESOL IN VIETNAM</div>
      <ul class="leader-points">
        <li><strong>Australian</strong> Government accredited</li>
        <li><strong>FREE</strong> accommodation in Ho Chi Minh City</li>
        <li><strong>Guaranteed</strong> teaching job at the end</li>
      </ul>
      <div class="leader-url">www.brightlarklessons-asia.com</div>
    </div>
  </section>

  <section class="banner half" aria-label="234 by 60 banner">
    <div class="brand"><span class="brand-dot" style="width:16px;height:16px"></span>Bright Lark Lessons Asia</div>
    <div class="half-url">www.brightlarklessons-asia.com</div>
  </section>

  <section class="banner rect" aria-label="300 by 250 banner">
    <svg class="rect-top" viewBox="0 0 275 160" aria-hidden="true"><path d="M0 0H275V76Q120 82 0 158Z" fill="#ffffff"/></svg>
    <div class="brand"><span class="brand-dot" style="width:28px;height:28px"></span>Bright Lark Lessons Asia</div>
    <div class="rect-copy">
      <p><strong>Australian</strong><br>Government accredited</p>
      <p><span class="big">FREE</span> <span class="mid">accommodation</span><br>in Ho Chi Minh City</p>
    </div>
    <div class="rect-guarantee"><strong>Guaranteed</strong> teaching job at the end</div>
    <div class="rect-url">www.brightlarklessons-asia.com</div>
  </section>
</body>
</html>
```